Calder Pizza - Takeout Menu Design

We are looking for a takeout menu design.
We are looking for a( 5" x 8.5" DOUBLE SIDED) flyer with our available pizza flavors
Must be easy to ready and not "busy"

Must include our logo (attached)
website: www.calderpizza.ca
address:
Fenwick Ridge Plaza
417, 318 9 Avenue SW
and the following details:
Visit our website for our complete appetizer, pasta, salad and catering menu.

Winner of this contest will also be offered to create a few print designs via printhive.

Please do not hesitate to ask any questions.

Target Market(s)

Business / Office clientele

Industry/Entity Type

Pizza place / specializing in corporate orders

Requirements
Must have
• Easy to read
Should not have
• Can not be busy or cluttered

```html
<!DOCTYPE html>
<html lang="en">
<head>
<meta charset="utf-8">
<title>Calder Pizza – Takeout Menu</title>
<link href="https://fonts.googleapis.com/css2?family=Poppins:wght@300;400;500;600;700;800&family=Zilla+Slab:wght@600;700&display=swap" rel="stylesheet">
<style>
:root{
  --red:#c1301f;
  --red-dark:#8e1d12;
  --ink:#1e1e1e;
  --yellow:#f7e84a;
  --white:#ffffff;
  --grey-box:#3c3c3c;
  --backdrop-top:#efebeb;
  --backdrop-bottom:#dedddd;
}
*{margin:0;padding:0;box-sizing:border-box}
html,body{width:1200px;height:1200px;overflow:hidden}
body{background:linear-gradient(var(--backdrop-top),var(--backdrop-bottom));font-family:"Poppins",sans-serif;color:var(--ink);position:relative}
.page{position:absolute;background:var(--white);overflow:hidden;box-shadow:0 2px 6px rgba(0,0,0,.12)}
.page--front{left:122px;top:210px;width:460px;height:782px}
.page--back{left:619px;top:210px;width:459px;height:780px}
.band{position:absolute;left:0;top:0}
.photo{position:absolute}
.brand{position:absolute;color:var(--white);font-family:"Poppins",sans-serif;font-weight:300;letter-spacing:1px;text-align:center;line-height:1}
.headline{position:absolute;left:0;width:460px;text-align:center;font-family:"Zilla Slab",serif;font-weight:700;font-size:42px;line-height:1;color:var(--white);text-shadow:2px 2px 0 var(--red-dark)}
.finest{position:absolute;left:92px;top:230px;width:276px;height:42px;background:var(--ink);color:var(--yellow);font-weight:800;font-size:25px;letter-spacing:2px;display:flex;align-items:center;justify-content:center}
.and-tag{position:absolute;left:352px;top:282px;background:var(--white);color:var(--red);font-weight:800;font-size:15px;padding:2px 6px;transform:rotate(-10deg);letter-spacing:1px}
.section-title{position:absolute;font-family:"Zilla Slab",serif;font-weight:700;line-height:1}
.label-pizza{position:absolute;background:var(--ink);color:var(--yellow);font-weight:800;display:flex;align-items:center;justify-content:center;letter-spacing:2px}
.size{position:absolute;color:var(--white);font-family:"Zilla Slab",serif;font-weight:700;font-size:17px;display:flex;align-items:center;justify-content:center}
.size--small{background:var(--red)}
.size--large{background:var(--grey-box)}
.item{position:absolute}
.item .row{position:relative;font-size:10px;font-weight:600;line-height:1.2;min-height:12px}
.item .nm{display:block}
.item .p1,.item .p2{position:absolute;top:0;font-weight:600}
.item .p2{right:0}
.item .ds{font-size:7.5px;font-weight:400;line-height:1.2;margin-top:3px;color:#2b2b2b}
.col-front{left:34px;width:254px}
.col-front .p1{left:168px}
.col-front .nm{max-width:160px}
.col-a{left:21px;width:219px}
.col-a .p1{left:135px}
.col-a .nm{max-width:130px}
.col-a .ds{max-width:222px}
.col-b{left:260px;width:177px}
.col-b .p1{left:94px}
.col-b .nm{max-width:92px}
.col-b .ds{max-width:160px}
.rule{position:absolute;height:0;border-top:1.5px dotted #333}
.feature{position:absolute;left:255px;top:620px;width:204px;height:68px;background:var(--red);color:var(--white)}
.feature .row{position:absolute;left:11px;top:8px;width:171px;font-size:10px;font-weight:600;line-height:1.25}
.feature .p1,.feature .p2{position:absolute;top:0;color:var(--yellow)}
.feature .p1{left:88px}
.feature .p2{right:0}
.feature .ds{position:absolute;left:11px;top:44px;font-size:7.5px;line-height:1.2}
.web{position:absolute;display:flex;align-items:center;gap:5px;font-weight:700;line-height:1}
.address{position:absolute;display:flex;align-items:center;gap:8px;font-size:9px;font-weight:500}
.note{position:absolute;font-size:10px;font-weight:400}
.promo{position:absolute;left:40px;top:721px;width:160px;font-size:10.5px;font-weight:700;line-height:1.25}
.thumb{position:absolute;top:750px;width:57px;height:57px;border-radius:50%}
</style>
</head>
<body>

<section class="page page--front" aria-label="Front of takeout menu">
  <svg class="band" width="460" height="440" viewBox="0 0 460 440" aria-hidden="true">
    <path d="M0 0H460V430C380 428 300 395 220 383C150 373 60 395 0 433Z" fill="var(--red)"/>
  </svg>
  <div class="photo" role="img" aria-label="Photo of pizza slices on a plate" style="left:-70px;top:-45px;width:170px;height:220px;border-radius:50%;background:radial-gradient(circle at 55% 55%,#e9a35c,#d97c45 55%,#c9d6e2 72%,#dfe7ef)"></div>
  <div class="photo" role="img" aria-label="Photo of a margherita pizza on a wooden board" style="left:366px;top:-40px;width:190px;height:190px;border-radius:50%;background:radial-gradient(circle,#d9573a 0,#e5a162 55%,#a06a3a 75%,#7a4f2a)"></div>
  <div class="brand" style="left:80px;top:28px;width:300px;font-size:31px">CALDER PIZZA</div>

  <div class="headline" style="top:105px">Freshly</div>
  <div class="headline" style="top:145px">Made Pizzas</div>
  <div class="headline" style="top:186px">Every Day</div>
  <div class="finest">WITH THE FINEST</div>
  <div class="headline" style="top:267px;left:-30px">Ingredients</div>
  <div class="and-tag">AND</div>
  <div class="headline" style="top:306px">Perfectly Melted</div>
  <div class="headline" style="top:348px">Mozzarella.</div>

  <svg class="photo" role="img" aria-label="Photo of a margherita pizza on a wooden peel" width="160" height="352" viewBox="0 0 160 352" style="left:300px;top:430px">
    <defs><radialGradient id="pizzaTone" cx="0.75" cy="0.38" r="0.6"><stop offset="0" stop-color="#d2452c"/><stop offset="0.55" stop-color="#e49a5a"/><stop offset="1" stop-color="#c08a4e"/></radialGradient></defs>
    <path d="M121 0A121 121 0 1 0 160 236V352H94V250A121 121 0 0 1 0 133A121 121 0 0 1 121 0Z" fill="url(#pizzaTone)"/>
  </svg>

  <div class="section-title" style="left:32px;top:410px;font-size:24px;color:var(--red)">Classic<br>Take-out</div>
  <div class="label-pizza" style="left:35px;top:458px;width:91px;height:32px;font-size:20px">PIZZA</div>
  <div class="size size--small" style="left:197px;top:458px;width:43px;height:31px">8"</div>
  <div class="size size--large" style="left:247px;top:458px;width:43px;height:31px">13"</div>

  <div class="item col-front" style="top:499px"><div class="row"><span class="nm">Pepperoni &amp; Mushroom</span><span class="p1">$12.99</span><span class="p2">$30.95</span></div></div>
  <div class="rule" style="left:37px;top:517px;width:251px"></div>
  <div class="item col-front" style="top:525px"><div class="row"><span class="nm">Pepperoni</span><span class="p1">$11.99</span><span class="p2">$29.95</span></div></div>
  <div class="rule" style="left:37px;top:543px;width:251px"></div>
  <div class="item col-front" style="top:552px"><div class="row"><span class="nm">Hawaiian</span><span class="p1">$12.99</span><span class="p2">$30.95</span></div></div>
  <div class="rule" style="left:37px;top:571px;width:251px"></div>
  <div class="item col-front" style="top:579px"><div class="row"><span class="nm">Beef &amp; Mushroom</span><span class="p1">$13.49</span><span class="p2">$32.95</span></div></div>
  <div class="rule" style="left:37px;top:598px;width:251px"></div>
  <div class="item col-front" style="top:606px"><div class="row"><span class="nm">Pepperoni &amp; Ham</span><span class="p1">$12.99</span><span class="p2">$30.95</span></div></div>
  <div class="rule" style="left:37px;top:625px;width:251px"></div>
  <div class="item col-front" style="top:633px"><div class="row"><span class="nm">Ham &amp; Mushroom</span><span class="p1">$12.99</span><span class="p2">$30.95</span></div></div>
  <div class="rule" style="left:37px;top:652px;width:251px"></div>
  <div class="item col-front" style="top:660px"><div class="row"><span class="nm">Beef &amp; Onion</span><span class="p1">$13.49</span><span class="p2">$32.95</span></div></div>
  <div class="rule" style="left:37px;top:680px;width:251px"></div>
  <div class="item col-front" style="top:689px"><div class="row"><span class="nm">Cheese</span><span class="p1">$11.99</span><span class="p2">$29.95</span></div></div>

  <div class="web" style="left:35px;top:723px;font-size:21px">
    <svg width="20" height="20" viewBox="0 0 20 20" aria-hidden="true"><g fill="none" stroke="var(--red)" stroke-width="1.4"><circle cx="10" cy="10" r="8.5"/><ellipse cx="10" cy="10" rx="3.8" ry="8.5"/><path d="M1.5 10H18.5M3 5.5H17M3 14.5H17"/></g></svg>
    <span>calderpizza.ca</span>
  </div>
  <div class="address" style="left:39px;top:751px">
    <svg width="13" height="16" viewBox="0 0 13 16" aria-hidden="true"><path d="M6.5 0A6 6 0 0 0 .5 6C.5 10.5 6.5 16 6.5 16S12.5 10.5 12.5 6A6 6 0 0 0 6.5 0Z" fill="var(--red)"/><circle cx="6.5" cy="6" r="2.2" fill="var(--white)"/></svg>
    <span>Fenwick Ridge Plaza, 417, 318 9 Avenue SW</span>
  </div>
</section>

<section class="page page--back" aria-label="Back of takeout menu">
  <svg class="band" width="459" height="130" viewBox="0 0 459 130" aria-hidden="true">
    <path d="M0 0H459V125C400 128 330 120 260 112C160 103 80 104 0 108Z" fill="var(--red)"/>
  </svg>
  <div class="section-title" style="left:20px;top:30px;font-size:30px;color:var(--yellow);text-shadow:1px 1px 0 var(--red-dark)">Speciality<br>Take-out</div>
  <div class="photo" role="img" aria-label="Photo of a margherita pizza on a wooden board" style="left:221px;top:-11px;width:136px;height:136px;border-radius:50%;background:radial-gradient(circle,#d9573a 0,#e5a162 55%,#a06a3a 78%,#7a4f2a)"></div>
  <div class="brand" style="left:360px;top:30px;width:80px;font-size:16px;line-height:1.1">CALDER<br>PIZZA</div>

  <div class="label-pizza" style="left:22px;top:94px;width:108px;height:42px;font-size:25px">PIZZA</div>
  <div class="size size--small" style="left:151px;top:102px;width:43px;height:32px">8"</div>
  <div class="size size--large" style="left:200px;top:102px;width:44px;height:32px">13"</div>
  <div class="size size--small" style="left:349px;top:102px;width:42px;height:32px">8"</div>
  <div class="size size--large" style="left:396px;top:102px;width:45px;height:32px">13"</div>

  <div class="item col-a" style="top:145px"><div class="row"><span class="nm">All Meat</span><span class="p1">$14.99</span><span class="p2">$35.95</span></div><p class="ds">Pepperoni, Beef &amp; Smoked Ham &amp; Bacon</p></div>
  <div class="rule" style="left:21px;top:176px;width:219px"></div>
  <div class="item col-a" style="top:182px"><div class="row"><span class="nm">Double Pepperoni</span><span class="p1">$13.49</span><span class="p2">$32.95</span></div><p class="ds">Loads of Pepperoni</p></div>
  <div class="rule" style="left:21px;top:211px;width:219px"></div>
  <div class="item col-a" style="top:221px"><div class="row"><span class="nm">Hot Honey Pepperoni</span><span class="p1">$14.49</span><span class="p2">$34.95</span></div><p class="ds">Double Pepperoni and drizzled with Hot Honey</p></div>
  <div class="rule" style="left:21px;top:247px;width:219px"></div>
  <div class="item col-a" style="top:257px"><div class="row"><span class="nm">Hawaiian Heat</span><span class="p1">$13.49</span><span class="p2">$32.95</span></div><p class="ds">Smoked Ham, Pineapple and Banana Peppers</p></div>
  <div class="rule" style="left:21px;top:286px;width:219px"></div>
  <div class="item col-a" style="top:293px"><div class="row"><span class="nm">Four Cheese</span><span class="p1">$13.49</span><span class="p2">$32.95</span></div><p class="ds">Mozzarella, Feta, Romano and Cheddar Cheese</p></div>
  <div class="rule" style="left:21px;top:322px;width:219px"></div>
  <div class="item col-a" style="top:328px"><div class="row"><span class="nm">Montreal</span><span class="p1">$13.49</span><span class="p2">$32.95</span></div><p class="ds">Pepperoni &amp; Double Smoked Bacon</p></div>
  <div class="rule" style="left:21px;top:356px;width:219px"></div>
  <div class="item col-a" style="top:362px"><div class="row"><span class="nm">Montreal Heat</span><span class="p1">$13.99</span><span class="p2">$33.95</span></div><p class="ds">Pepperoni, Double Smoked Bacon &amp; Banana Peppers</p></div>
  <div class="rule" style="left:21px;top:391px;width:219px"></div>
  <div class="item col-a" style="top:398px"><div class="row"><span class="nm">Supreme</span><span class="p1">$13.49</span><span class="p2">$32.95</span></div><p class="ds">Pepperoni, Mushrooms &amp; Green Peppers</p></div>
  <div class="rule" style="left:21px;top:426px;width:219px"></div>
  <div class="item col-a" style="top:433px"><div class="row"><span class="nm">Canadian</span><span class="p1">$13.49</span><span class="p2">$32.95</span></div><p class="ds">Pepperoni, Mushrooms &amp; Ham</p></div>
  <div class="rule" style="left:21px;top:462px;width:219px"></div>
  <div class="item col-a" style="top:470px"><div class="row"><span class="nm">BBQ Chicken</span><span class="p1">$13.99</span><span class="p2">$33.95</span></div><p class="ds">Chicken Breast, Hickory BBQ Sauce &amp; Red Onions</p></div>
  <div class="rule" style="left:21px;top:499px;width:219px"></div>
  <div class="item col-a" style="top:509px"><div class="row"><span class="nm">BBQ Chicken Plus</span><span class="p1">$14.79</span><span class="p2">$34.95</span></div><p class="ds">Chicken Breast, Hickory BBQ Sauce, Red Onions &amp; Cilantro</p></div>
  <div class="rule" style="left:21px;top:538px;width:219px"></div>
  <div class="item col-a" style="top:546px"><div class="row"><span class="nm">Spicy BBQ Chicken</span><span class="p1">$14.49</span><span class="p2">$35.95</span></div><p class="ds" style="max-width:190px">Chicken Breast, Hickory BBQ Sauce, Red Onions &amp; Banana Peppers</p></div>
  <div class="rule" style="left:21px;top:585px;width:219px"></div>
  <div class="item col-a" style="top:593px"><div class="row"><span class="nm">Sweet Chili Chicken</span><span class="p1">$14.49</span><span class="p2">$35.95</span></div><p class="ds" style="max-width:150px">Chicken Breast, Pineapple, Red Onions &amp; Sweet Chili Sauce</p></div>
  <div class="rule" style="left:21px;top:629px;width:219px"></div>
  <div class="item col-a" style="top:636px"><div class="row"><span class="nm">Chicken Club</span><span class="p1">$14.79</span><span class="p2">$35.95</span></div><p class="ds" style="max-width:200px">Chicken Breast, Double Smoked Bacon, Red Onions and Tomatoes</p></div>
  <div class="rule" style="left:21px;top:672px;width:219px"></div>
  <div class="item col-a" style="top:680px"><div class="row"><span class="nm">Athenean</span><span class="p1">$14.49</span><span class="p2">$34.95</span></div><p class="ds">Chicken Breast, Spinach, Feta Cheese and Tomato</p></div>

  <div class="item col-b" style="top:146px"><div class="row"><span class="nm">Greek Supreme</span><span class="p1">$14.99</span><span class="p2">$35.95</span></div><p class="ds">Chicken Breast, Feta Cheese, Tomato, Green Pepper, Red Onions &amp; Black Olives</p></div>
  <div class="rule" style="left:260px;top:188px;width:177px"></div>
  <div class="item col-b" style="top:194px"><div class="row"><span class="nm">Mediterranean Chicken</span><span class="p1">$14.79</span><span class="p2">$35.95</span></div><p class="ds">Chicken Breast, Feta Cheese, Tomato, Green Pepper, Red Onions &amp; Black Olives</p></div>
  <div class="rule" style="left:260px;top:248px;width:177px"></div>
  <div class="item col-b" style="top:254px"><div class="row"><span class="nm">Original Spinach</span><span class="p1">$13.49</span><span class="p2">$32.95</span></div><p class="ds">Spinach &amp; Feta Cheese</p></div>
  <div class="rule" style="left:260px;top:287px;width:177px"></div>
  <div class="item col-b" style="top:293px"><div class="row"><span class="nm">Zeus</span><span class="p1">$13.95</span><span class="p2">$33.95</span></div><p class="ds">Spinach, Feta Cheese and Tomatoes</p></div>
  <div class="rule" style="left:260px;top:324px;width:177px"></div>
  <div class="item col-b" style="top:331px"><div class="row"><span class="nm">Greek</span><span class="p1">$13.99</span><span class="p2">$33.95</span></div><p class="ds">Feta Cheese, Tomato, Green Peppers, Red Onions and Black Olives</p></div>
  <div class="rule" style="left:260px;top:374px;width:177px"></div>
  <div class="item col-b" style="top:380px"><div class="row"><span class="nm">Vegetarian</span><span class="p1">$13.49</span><span class="p2">$32.95</span></div><p class="ds">Mushrooms, Tomatoes, Green Peppers and Black Olives</p></div>
  <div class="rule" style="left:260px;top:421px;width:177px"></div>
  <div class="item col-b" style="top:426px"><div class="row"><span class="nm">Veggie Delight</span><span class="p1">$13.95</span><span class="p2">$33.95</span></div><p class="ds">Spinach &amp; Feta Cheese</p></div>
  <div class="rule" style="left:260px;top:460px;width:177px"></div>
  <div class="item col-b" style="top:464px"><div class="row"><span class="nm">Deluxe</span><span class="p1">$14.49</span><span class="p2">$34.95</span></div><p class="ds">Pepperoni, Mushrooms, Ham, Tomatoes, Green Peppers and Red Onions</p></div>
  <div class="rule" style="left:260px;top:504px;width:177px"></div>
  <div class="item col-b" style="top:509px"><div class="row"><span class="nm">Calder Special</span><span class="p1">$14.49</span><span class="p2">$34.95</span></div><p class="ds">Pepperoni, Mushrooms, Ham, Green Peppers and Black Olives</p></div>
  <div class="rule" style="left:260px;top:552px;width:177px"></div>
  <div class="item col-b" style="top:558px"><div class="row" style="min-height:26px"><span class="nm">Dill Pickle</span><span class="p1">$13.49<br>$32.95</span><span class="p2">$14.49<br>$35.95</span></div><p class="ds">Crispy Dill Pickles, Fresh Dill with our cream based garlic sauce. Served with our without bacon</p></div>

  <div class="feature">
    <div class="row"><span class="nm">BBQ<br>Pulled Pork</span><span class="p1">$14.49</span><span class="p2">$33.95</span></div>
    <p class="ds">Pulled Pork, Red Onions, Red Peppers<br>and Cilantro</p>
  </div>
  <div class="note" style="left:352px;top:695px">GST not included</div>

  <p class="promo">Check out our website to explore our full menu of appetizers, pastas, salads, and catering options!</p>
  <div class="web" style="left:214px;top:719px;font-size:21px;color:var(--red)">
    <svg width="20" height="20" viewBox="0 0 20 20" aria-hidden="true"><g fill="none" stroke="var(--red)" stroke-width="1.4"><circle cx="10" cy="10" r="8.5"/><ellipse cx="10" cy="10" rx="3.8" ry="8.5"/><path d="M1.5 10H18.5M3 5.5H17M3 14.5H17"/></g></svg>
    <span>calderpizza.ca</span>
  </div>
  <div class="thumb" role="img" aria-label="Photo of appetizers" style="left:219px;background:radial-gradient(circle,#d99a55,#b9c2c8)"></div>
  <div class="thumb" role="img" aria-label="Photo of a pasta dish" style="left:291px;background:radial-gradient(circle,#f0e3c2,#d69a4a)"></div>
  <div class="thumb" role="img" aria-label="Photo of a fresh salad" style="left:363px;background:radial-gradient(circle,#d9452f,#6aa443)"></div>
</section>

</body>
</html>
```